Vell Datacraft Halloween Imagery

I work for a growing IT company and we are running a local social media campaign through which we are asking customers and prospects to design a jack-o-lantern as creatively as they please but to integrate our logo. We'd like this asset (or assets) to be the creative cornerstone of a social media card as well as an announcement about the pumpkin carving contest. Please take a look at our website and our brand guidelines

https://www.velldatacraft.example/
https://kitvaultly.example/s/qmzrua-h72k81-7bx40d
Logos: https://kitvaultly.example/s/qmzrw3-kdtvn-8owrb2

```html
<!DOCTYPE html>
<html lang="en">
<head>
<meta charset="utf-8">
<title>Vell Datacraft — Pumpkin Carving Contest</title>
<link rel="stylesheet" href="https://fonts.googleapis.com/css2?family=Montserrat:wght@600&family=Emilys+Candy&display=swap">
<style>
  :root {
    --page: #ffffff;
    --night: #050405;
    --night-soft: #1a120c;
    --pumpkin: #f07a1e;
    --pumpkin-deep: #c2400e;
    --soil: #2e1f12;
    --wood: #c8742a;
    --wood-dark: #7a3e12;
    --board: #262b4e;
    --chalk-orange: #f2721f;
    --brand-mark: #f4591f;
    --white: #ffffff;
  }
  * { margin: 0; padding: 0; box-sizing: border-box; }
  html, body {
    width: 1200px;
    height: 732px;
    overflow: hidden;
    background: var(--page);
  }
  .social-card {
    position: relative;
    width: 1200px;
    height: 732px;
    background: var(--page);
  }
  .hero {
    position: absolute;
    left: 135px;
    top: 80px;
    width: 930px;
    height: 572px;
    overflow: hidden;
    background:
      radial-gradient(ellipse 340px 230px at 160px 360px, var(--pumpkin) 0%, var(--pumpkin-deep) 45%, rgba(194,64,14,0) 100%),
      radial-gradient(ellipse 220px 160px at 330px 250px, rgba(240,122,30,0.85) 0%, rgba(194,64,14,0) 100%),
      linear-gradient(180deg, var(--night) 0%, var(--night) 55%, var(--night-soft) 80%, var(--soil) 100%);
  }
  .hero-scene {
    position: absolute;
    inset: 0;
  }
  .brand {
    position: absolute;
    left: 465px;
    top: 56px;
    display: flex;
    align-items: center;
    gap: 14px;
  }
  .brand-square {
    width: 52px;
    height: 52px;
    background: var(--brand-mark);
  }
  .brand-name {
    font-family: "Montserrat", sans-serif;
    font-weight: 600;
    font-size: 30px;
    letter-spacing: 0.5px;
    color: var(--white);
    text-transform: uppercase;
  }
  .contest-sign {
    position: absolute;
    left: 437px;
    top: 182px;
    width: 406px;
    height: 328px;
    border: 22px solid var(--wood);
    border-color: var(--wood) var(--wood-dark) var(--wood-dark) var(--wood);
    background: var(--board);
    box-shadow: 0 10px 30px rgba(0,0,0,0.6);
    display: flex;
    flex-direction: column;
    align-items: center;
    justify-content: center;
    text-align: center;
    color: var(--chalk-orange);
    font-family: "Emilys Candy", cursive;
    line-height: 1;
  }
  .sign-title {
    font-size: 60px;
    letter-spacing: 1px;
    margin-bottom: 8px;
  }
  .sign-subtitle {
    font-size: 58px;
    margin-bottom: 6px;
  }
</style>
</head>
<body>
  <main class="social-card">
    <section class="hero">
      <div class="hero-scene" role="img" aria-label="Night scene of glowing carved paper jack-o-lanterns resting on dark soil beside bare twigs"></div>

      <div class="brand">
        <span class="brand-square"></span>
        <span class="brand-name">Vell Datacraft</span>
      </div>

      <div class="contest-sign">
        <h1 class="sign-title">PUMPKIN</h1>
        <p class="sign-subtitle">Carving</p>
        <p class="sign-subtitle">Contest</p>
      </div>
    </section>
  </main>
</body>
</html>
```